Design a Bold Tradeshow Backdrop for a Sustainable Cleaning Technology

We need a professional, high-impact 10' × 8' tradeshow backdrop for Veldrix®, a commercial cleaning technology company. 143.75" x 90" high and needs bleeds in the 143.75" direction for printing but the graphic area is 10' wide.

Our first event will have an audience that includes K–12 school administrators, facility managers, business officials, and custodial decision-makers. However, this backdrop will be used at multiple future trade shows across different commercial and institutional markets.

The design therefore needs to be universal rather than specifically education- or school-themed.

Our goal is to stop attendees as they walk past the booth and immediately communicate a simple message:

Safer and more sustainable cleaning can also cost substantially less than conventional cleaning chemicals.

We want the design to feel modern, innovative, clean, sustainable, credible, commercial, and premium. It should resonate with K–12 decision-makers while being equally appropriate at events serving commercial facilities, healthcare, hospitality, government, property management, transportation, and other institutional markets.

It should NOT look like a traditional janitorial supply advertisement and should not be overly busy.

The most important messages need to be understandable from approximately 10–20 feet away.

Required Messaging

The primary headline should be:

SUSTAINABLE CLEANING
DOES NOT HAVE TO BE EXPENSIVE.

Three major value propositions should be prominently displayed:

FREE
Cleaning Chemical Analysis
See how much you can save.

SAVE UP TO 60% or More
on Cleaning Chemical Costs

AS LITTLE AS $0.27/GALLON

We would also like a strong secondary message incorporated into the design:

SMARTER CLEANING.
High Performance. Low Cost. Safer.

Visual Direction — Important

Rather than showing a K–12 school hallway or other environment that limits the backdrop to the education market, we want a sophisticated, universal commercial or institutional environment.

This could be a bright, contemporary commercial facility, lobby, corridor, office environment, public building, or other premium architectural space that could reasonably represent many different types of facilities.

The environment should communicate:

Cleanliness • Safety • Sustainability • Professionalism • Efficiency • High Performance

We want someone from a school, hospital, hotel, office building, airport, government facility, or other commercial property to be able to look at the backdrop and relate the imagery to their own facility.

Please avoid imagery that makes the backdrop industry-specific.

We also want to avoid clichéd environmental imagery. The design does not need to be covered in leaves, trees, water droplets, recycling symbols, or other obvious "green" graphics to communicate sustainability. We prefer a sophisticated commercial interpretation of sustainability.

Color & Brand Direction

We want the overall color palette to stay primarily within:

Blues — consistent with our corporate identity

Greens — to reinforce sustainability, safety, efficiency, and environmental responsibility

White — strongly encouraged for clean space, contrast, and an open contemporary appearance

Black — should be limited primarily to text where necessary for readability

Please avoid making black a major background or dominant design color.

We want the finished display to have a bright, clean, sophisticated, sustainable look and feel rather than a dark or industrial appearance.

The design should use significant negative space and a strong visual hierarchy.

Less is more.

We prefer a few large, powerful messages that can be understood quickly rather than numerous small bullet points, paragraphs, or icons.

Creative Freedom

The attached concept image is provided to communicate our general direction and messaging only.

It does not need to be copied.

We are specifically running this contest because we want designers to improve upon our initial concept and show us different creative approaches to presenting the Veldrix value proposition.

We are open to creative interpretations of the commercial environment, composition, typography, use of negative space, and how the three major financial benefits are presented.

The finished design should feel like an innovative commercial technology brand, not simply another cleaning chemical company.

Corporate Logo — Very Important

We are attaching our official Veldrix® corporate logo for use in the design.

DO NOT redraw, recreate, modify, stylize, reinterpret, trace, or AI-generate the Veldrix logo.

The supplied corporate logo must be inserted directly into the artwork exactly as provided, maintaining its original proportions, colors, typography, trademark elements, and graphic design.

The logo should generally appear in the upper-left area of the backdrop but should not overwhelm the primary marketing message.

Printer Template & Graphic Sizing

We are also attaching the printer's official graphic template and instructions for the 8' × 8' tension-fabric display.

Designers should create their artwork using these supplied specifications so the winning design can be transferred directly into production.

The printer requires that the original document size not be changed, artwork be created on the designated design layer or a new layer, images be embedded, text be converted to outlines, and the finished production artwork be supplied as a PDF.

Please pay particular attention to the bleed area, finished size, and safe artwork area when positioning important text, graphics, and the corporate logo.

Physical Booth Context

The backdrop will sit behind an 8' tradeshow table.

The complete booth will also contain:

A blue stretch tablecloth with the Veldrix corporate logo
Morvaqs and Veldrix product containers and samples on the table
An Lunadrav chemical mixing/dilution station displayed on an elevated stand to the left
A television/monitor to the right demonstrating our online ROI cost-savings calculator

Because these other booth elements will explain our products and technology in greater detail, the backdrop should NOT attempt to explain everything we do.

Its primary purpose is to stop traffic, establish the Veldrix brand, and communicate our core economic and sustainability value proposition.

Final Deliverables

The winning designer must provide artwork properly sized and positioned using our supplied 8' × 8' tension-fabric display template.

Final files should include:

Print-ready, high-resolution PDF
Editable source/vector artwork
All images embedded
Fonts converted to outlines
Artwork correctly positioned within the supplied printer template
Original Veldrix corporate logo incorporated without modification
The 3–5 Second Test

This is perhaps the most important requirement.

Someone walking down a tradeshow aisle should be able to look at the backdrop for 3–5 seconds and understand:

Veldrix offers safer, sustainable, high-performance commercial cleaning — at a lower cost.

The three offers we particularly want them to remember are:

FREE CHEMICAL ANALYSIS

SAVE UP TO 60%

AS LITTLE AS $0.27/GALLON

The overall takeaway should be:

Sustainable cleaning does not have to cost more.

We want the winning design to make that message immediately understandable, credible, and memorable.

Colors
0054AA
0677BA
7BADD7
CADEEF
E8F1F8
0094D4
00A9DD
6FCCEA
C7EBF8
E9F6FB
00AB8E
00BBA5
67D7C9
C6EFE9
E9F9F6
59FF00
82FF00
B8FF75
E3FFCB
F4FFEA

```html
<!DOCTYPE html>
<html lang="en">
<head>
<meta charset="utf-8">
<title>Veldrix Tradeshow Backdrop</title>
<link rel="stylesheet" href="https://fonts.googleapis.com/css2?family=Poppins:wght@400;500;600;700&family=Roboto:wght@700;900&display=swap">
<style>
  :root {
    --navy: #1b3a6b;
    --ink: #0f1f5c;
    --green: #6aa83a;
    --lime: #8cc84b;
    --white: #ffffff;
  }
  * { box-sizing: border-box; margin: 0; padding: 0; }
  html, body { width: 1200px; height: 1200px; overflow: hidden; background: var(--white); }
  .backdrop { position: relative; width: 1200px; height: 1200px; background: var(--white); font-family: "Poppins", sans-serif; }

  .hero-photo {
    position: absolute; left: 0; top: 0; width: 1200px; height: 560px;
    background:
      linear-gradient(180deg, rgba(255,255,255,0) 55%, #ffffff 100%),
      linear-gradient(90deg, #c9a98a 0%, #efe6dc 22%, #f7f4f0 50%, #efe6dc 78%, #c9a98a 100%);
  }

  .brand-tab {
    position: absolute; left: 454px; top: 0; width: 292px; height: 201px;
    background: var(--white); border-radius: 0 0 24px 24px;
    box-shadow: 0 4px 14px rgba(0,0,0,0.12);
    display: flex; align-items: center; justify-content: center;
  }
  .brand-word { font-family: "Poppins", sans-serif; font-weight: 700; font-size: 54px; color: var(--navy); line-height: 1; }

  .headline { position: absolute; left: 0; width: 1200px; text-align: center; font-family: "Roboto", sans-serif; font-weight: 900; line-height: 1; }
  .headline-top { top: 527px; font-size: 66px; color: var(--green); letter-spacing: 0.5px; }
  .headline-bottom { top: 597px; font-size: 65px; color: var(--navy); }

  .offer { position: absolute; top: 735px; width: 305px; height: 202px; border: 2px solid var(--ink); border-radius: 12px; background: var(--white); }
  .offer-head {
    height: 93px; border-radius: 10px 10px 0 0;
    background: linear-gradient(180deg, #0d2f7a 0%, #0a0d52 100%);
    display: flex; align-items: center; justify-content: center; color: var(--white);
  }
  .offer-body { height: 105px; display: flex; flex-direction: column; align-items: center; justify-content: center; text-align: center; color: var(--ink); font-size: 18px; line-height: 1.3; }
  .offer-number {
    position: absolute; top: -21px; left: 50%; margin-left: -21px; width: 42px; height: 42px; border-radius: 50%;
    border: 3px solid var(--white); background: linear-gradient(135deg, var(--lime), #143a6b);
    color: var(--white); font-weight: 700; font-size: 24px; display: flex; align-items: center; justify-content: center;
  }
  .offer-free { left: 86px; }
  .offer-save { left: 455px; }
  .offer-price { left: 818px; }
  .free-word { font-family: "Roboto", sans-serif; font-weight: 900; font-size: 54px; color: var(--lime); }
  .save-lead { font-weight: 700; font-size: 22px; line-height: 0.95; margin-right: 10px; }
  .save-value { font-weight: 700; font-size: 56px; color: var(--lime); }
  .price-lead { font-size: 18px; font-weight: 500; letter-spacing: 0.5px; }
  .price-value { font-weight: 700; font-size: 52px; color: var(--ink); line-height: 1; }
  .price-value sup { font-size: 24px; vertical-align: 22px; }
  .price-unit { font-size: 18px; margin-top: 6px; }

  .value-band { position: absolute; left: 0; top: 993px; width: 1200px; height: 207px; display: flex; }
  .value-list { position: relative; width: 631px; height: 100%; background: linear-gradient(90deg, #1b3568 0%, #2e5a70 45%, #8cc84b 100%); }
  .value-col { position: absolute; top: 36px; list-style: none; }
  .value-col li { display: flex; align-items: center; gap: 10px; height: 49px; color: var(--white); font-size: 28px; font-weight: 400; }
  .value-col svg { width: 23px; height: 23px; flex: none; }
  .value-col-left { left: 55px; }
  .value-col-right { left: 329px; }
  .value-divider { position: absolute; left: 297px; top: 28px; width: 1px; height: 156px; background: rgba(255,255,255,0.6); }

  .smarter { position: relative; flex: 1; background: linear-gradient(90deg, #0f2369 0%, #0a0d52 100%); color: var(--white); }
  .smarter-title { position: absolute; left: 0; width: 100%; top: 22px; text-align: center; font-weight: 700; font-size: 42px; letter-spacing: 0.5px; }
  .smarter-item { position: absolute; top: 104px; text-align: center; font-size: 22px; line-height: 1.5; }
  .smarter-performance { left: 60px; width: 160px; }
  .smarter-cost { left: 280px; width: 90px; }
  .smarter-safer { left: 420px; width: 90px; top: 100px; }
  .smarter-divider { position: absolute; top: 112px; width: 1px; height: 55px; background: rgba(255,255,255,0.7); }
  .smarter-divider-a { left: 260px; }
  .smarter-divider-b { left: 400px; }
</style>
</head>
<body>
<main class="backdrop">
  <div class="hero-photo" role="img" aria-label="Bright marble-columned lobby corridor with polished reflective floor, fading to white"></div>

  <header class="brand-tab">
    <span class="brand-word">Veldrix</span>
  </header>

  <h1 class="headline headline-top">SUSTAINABLE CLEANING</h1>
  <h2 class="headline headline-bottom">DOES NOT HAVE TO BE EXPENSIVE</h2>

  <section class="offer offer-free">
    <div class="offer-number">1</div>
    <div class="offer-head"><span class="free-word">FREE</span></div>
    <div class="offer-body">Cleaning Chemical<br>Analysis See how<br>much you can save.</div>
  </section>

  <section class="offer offer-save">
    <div class="offer-number">2</div>
    <div class="offer-head"><span class="save-lead">SAVE<br>UP TO</span><span class="save-value">60%</span></div>
    <div class="offer-body">or More on Cleaning<br>Chemical Costs</div>
  </section>

  <section class="offer offer-price">
    <div class="offer-number">3</div>
    <div class="offer-head"><span class="price-lead">AS LITTLE AS</span></div>
    <div class="offer-body">
      <div class="price-value"><sup>$</sup>0.27</div>
      <div class="price-unit">/GALLON</div>
    </div>
  </section>

  <footer class="value-band">
    <div class="value-list">
      <ul class="value-col value-col-left">
        <li><svg viewBox="0 0 24 24"><circle cx="12" cy="12" r="11" fill="#fff"/><path d="M6.5 12.5l3.6 3.5 7.4-7.5" fill="none" stroke="#1b3568" stroke-width="2.8" stroke-linecap="round" stroke-linejoin="round"/></svg>Cleanliness</li>
        <li><svg viewBox="0 0 24 24"><circle cx="12" cy="12" r="11" fill="#fff"/><path d="M6.5 12.5l3.6 3.5 7.4-7.5" fill="none" stroke="#1b3568" stroke-width="2.8" stroke-linecap="round" stroke-linejoin="round"/></svg>Safety</li>
        <li><svg viewBox="0 0 24 24"><circle cx="12" cy="12" r="11" fill="#fff"/><path d="M6.5 12.5l3.6 3.5 7.4-7.5" fill="none" stroke="#1b3568" stroke-width="2.8" stroke-linecap="round" stroke-linejoin="round"/></svg>Sustainability</li>
      </ul>
      <div class="value-divider"></div>
      <ul class="value-col value-col-right">
        <li><svg viewBox="0 0 24 24"><circle cx="12" cy="12" r="11" fill="#fff"/><path d="M6.5 12.5l3.6 3.5 7.4-7.5" fill="none" stroke="#2e5a70" stroke-width="2.8" stroke-linecap="round" stroke-linejoin="round"/></svg>Professionalism</li>
        <li><svg viewBox="0 0 24 24"><circle cx="12" cy="12" r="11" fill="#fff"/><path d="M6.5 12.5l3.6 3.5 7.4-7.5" fill="none" stroke="#2e5a70" stroke-width="2.8" stroke-linecap="round" stroke-linejoin="round"/></svg>Efficiency</li>
        <li><svg viewBox="0 0 24 24"><circle cx="12" cy="12" r="11" fill="#fff"/><path d="M6.5 12.5l3.6 3.5 7.4-7.5" fill="none" stroke="#2e5a70" stroke-width="2.8" stroke-linecap="round" stroke-linejoin="round"/></svg>High Performance</li>
      </ul>
    </div>
    <div class="smarter">
      <div class="smarter-title">SMARTER CLEANING</div>
      <div class="smarter-item smarter-performance">High<br>Performance</div>
      <div class="smarter-divider smarter-divider-a"></div>
      <div class="smarter-item smarter-cost">Low<br>Cost</div>
      <div class="smarter-divider smarter-divider-b"></div>
      <div class="smarter-item smarter-safer">Safer</div>
    </div>
  </footer>
</main>
</body>
</html>
```